依頼詳細
◆サイトマップ
01.ホーム
02.当院について
03.医院紹介
04.スタッフ紹介
05.初めての方へ
06.銀歯から自然な白い歯へ
07.歯医者にいけなくなった方へ
08.歯の色を全体的に白くしたい方へ
09.口臭が気になる・歯茎に違和感がある
10.歯並びを整えたい方へ
11.歯が失ってしまった方へ
12.虫歯になってしまった方へ
13.お子様の歯を守りたい方へ
14.求人情報
15.よくあるご質問
16.問い合わせ
17.お知らせ(一覧)
18.お知らせ(詳細)
19.ブログ(一覧)
20.ブログ(詳細)

◆TOPに掲載いただきたいもの
・ヘッダー、ロゴ、営業時間、電話番号
・グローバルナビ
・メインイメージ
・お知らせの新着ボックス
・コンセプト
・強み
・各症状ページへ流入する箇所(サイトマップ06~13の内容)
・その他下層ページ移行用バナー(よくあるご質問、問い合わせ、求人情報)
・ブログの新着ボックス
・グーグルマップ
・フッター(ロゴ、院情報、営業時間、サイトマップ)
※仮で作成したもののためレイアウトの並びはお任せ致します。
ただし、配置してあるコンテンツはすべて含まれるようにしてください。
提案で項目を追加頂く等は参考にさせて頂きたいので大変嬉しいです。

◆デザインについて
・希望するイメージ
知的/清潔な/高級感

・希望デザインカラー
茶系
ベースは白やベージュ系

◆参考URL
https://miharadentalroom.example/
スペースのとり方に高級感を感じとても見やすい印象
TOPのコンテンツ量が少ないと感じる
サイトURL
http://203.0.113.47
ページ数
1ページ
希望イメージ
シンプル 複雑
単色 カラフル
暗い 明るい
日常 高級
遊び心 厳粛
未来的 伝統的
女性的 男性的
希望する色
茶系、ベースは白やベージュ系
納品ファイル
• イラストレーター形式 (.ai)
• フォトショップ形式 (.psd)
補足説明
◆素材について
素材として必要なものがある場合には、Lumira Stock画像をご使用ください。
その際、通常アセットでダウンロード出来る画像のみを使用してください。
Lumira Stock以外の素材を使用する際には、
必ず無料で提供いただける物のみご使用ください。
※現在、写真の用意がないのですが、撮影後に差し替える予定です。
イメージとしてLumira Stock画像を使用して作成ください。

◆ロゴ、外観、内観写真について
下記よりダウンロードしてご使用ください。
https://27.fileparcel.example/0811-b83c572e19a04df6c8e1b7a45d20e3f18
PASS:krvo
もう少し提案が見たいため、延長させて頂きます。
参考サイトを無視した少し奇抜なアイデアも見てみたいです。

院内で検討の上、決定致しました。
修正等も快諾いただき大変助かりました。

皆様たくさんのご提案ありがとうございました。

```html
<!DOCTYPE html>
<html lang="ja">
<head>
<meta charset="utf-8">
<title>霧野台デンタルクリニック</title>
<link href="https://fonts.googleapis.com/css2?family=Cormorant+Garamond:wght@400;500;600&family=Noto+Serif+JP:wght@400;500;600&display=swap" rel="stylesheet">
<style>
:root{
  --brown:#9b7d52;
  --brown-dark:#7d6340;
  --gold:#b39464;
  --beige:#f8efea;
  --cream:#fbf7f3;
  --ink:#4a4036;
  --muted:#8a7e72;
  --line:#d9ccbd;
  --white:#ffffff;
}
*{box-sizing:border-box;margin:0;padding:0}
html,body{width:1200px;height:5372px;overflow:hidden}
body{position:relative;background:var(--white);color:var(--ink);font-family:"Noto Serif JP",serif;font-size:14px;line-height:1.9}
.en{font-family:"Cormorant Garamond",serif;letter-spacing:.12em}
.abs{position:absolute}
.photo{position:absolute}
.btn{display:inline-block;background:var(--brown);color:var(--white);font-family:"Cormorant Garamond",serif;font-size:14px;letter-spacing:.2em;width:120px;height:32px;line-height:32px;text-align:center}
.sec-title{position:absolute;left:0;width:1200px;text-align:center}
.sec-title .en{display:block;font-size:22px;color:var(--gold)}
.sec-title .ja{display:block;font-size:12px;color:var(--muted);letter-spacing:.2em}
.sec-title::after{content:"";display:block;width:40px;height:1px;background:var(--gold);margin:8px auto 0}

/* header */
.hero{left:0;top:0;width:1200px;height:728px;background:linear-gradient(100deg,#6e5236 0%,#b8a088 28%,#ece4da 50%,#cfc2b2 70%,#5a4a3a 100%)}
.header-bar{left:0;top:0;width:1200px;height:56px;background:rgba(255,255,255,.92)}
.clinic-name{display:flex;align-items:center;gap:10px;font-family:"Noto Serif JP",serif;font-weight:500;white-space:nowrap}
.clinic-name i{display:block;width:10px;height:10px;background:currentColor}
.logo{left:40px;top:14px;height:28px;font-size:18px;color:var(--brown-dark);letter-spacing:.08em}
.gnav{right:150px;top:16px;display:flex;gap:18px;font-size:11px;color:var(--ink)}
.tel-btn{right:0;top:0;width:140px;height:40px;background:var(--brown);color:var(--white);font-size:11px;text-align:center;line-height:40px}
.hours{right:20px;top:60px;width:250px;background:rgba(60,45,30,.55);color:var(--white);font-size:10px;border-collapse:collapse}
.hours td,.hours th{padding:4px 3px;text-align:center;font-weight:400;border-bottom:1px solid rgba(255,255,255,.3)}
.hero-copy{left:0;top:320px;width:1200px;text-align:center;color:var(--white);font-family:"Noto Serif JP",serif;font-weight:400;font-size:40px;letter-spacing:.2em;line-height:1.4}

/* news */
.news{left:300px;top:652px;width:612px;height:208px;background:var(--white);box-shadow:0 4px 20px rgba(80,60,40,.12);padding:24px 40px}
.news h2{position:absolute;left:40px;top:22px;font-family:"Cormorant Garamond",serif;font-weight:500;font-size:18px;color:var(--gold);letter-spacing:.15em}
.news ul{list-style:none;margin-left:110px;font-size:11px}
.news li{border-bottom:1px dotted var(--line);padding:4px 0;white-space:nowrap}
.news li time{color:var(--gold);margin-right:16px}
.news .btn{position:absolute;left:40px;bottom:22px;width:84px;height:24px;line-height:24px;font-size:11px}

/* greeting */
.greet-panel{left:440px;top:1030px;width:760px;height:350px;background:var(--beige)}
.greet-photo{left:220px;top:1020px;width:212px;height:260px;background:linear-gradient(160deg,#b7c2c9,#6f7f8c)}
.greet-text{left:560px;top:1100px;width:560px;font-size:11px;line-height:2}
.greet-text h2{font-family:"Cormorant Garamond",serif;font-weight:500;color:var(--gold);font-size:20px;letter-spacing:.15em}
.greet-text h3{font-size:11px;color:var(--muted);font-weight:400;margin-bottom:14px}
.greet-text .sign{text-align:right;margin-top:8px}

/* concept */
.concept{left:0;top:1460px;width:1200px;height:340px;background:linear-gradient(90deg,#e9e2da,#f6f2ed 40%,#f3eee8 60%,#e2d8cc)}
.concept-list{left:400px;top:1560px;width:400px;list-style:none}
.concept-list li{border-bottom:1px solid var(--line);padding:6px 0;font-size:13px;text-align:left}
.concept-list li:nth-child(2){margin-left:20px}
.concept-list li:nth-child(3){margin-left:40px}
.concept-list li b{font-family:"Cormorant Garamond",serif;font-size:22px;color:var(--gold);font-weight:500;margin-right:8px}

/* features */
.feature-bg{left:0;top:1800px;width:1200px;height:1120px;background:linear-gradient(180deg,var(--white),var(--beige) 60%,var(--white))}
.feat-photo1{left:0;top:2000px;width:780px;height:400px;background:linear-gradient(110deg,#4c3a2a,#a58a6a 50%,#d9c9b4)}
.feat-photo2{left:500px;top:2448px;width:700px;height:400px;background:linear-gradient(250deg,#5a4634,#b39a7c 50%,#e6dccf)}
.feat-box{width:500px;background:var(--white);box-shadow:0 4px 20px rgba(80,60,40,.12);padding:30px 34px;font-size:11px;line-height:2}
.feat-box h3{font-size:16px;font-weight:500;border-bottom:1px solid var(--line);padding-bottom:8px;margin-bottom:12px}
.feat-box .btn{margin-top:16px;width:110px;height:28px;line-height:28px;font-size:12px}

/* medical */
.medical{left:0;top:2960px;width:1200px;height:660px;background:linear-gradient(90deg,#e7edf0,#f9f9f8 35%,#fbfaf8 65%,#f2ebe3)}
.med-grid{left:320px;top:3080px;width:580px;display:grid;grid-template-columns:repeat(4,144px);gap:28px 4px}
.med-item{width:144px;height:144px;border-radius:50%;background:var(--brown);color:var(--white);text-align:center;font-size:11px;line-height:1.5;padding-top:34px}
.med-item svg{display:block;margin:0 auto 8px}
.first-visit{left:288px;top:3420px;width:624px;height:160px;background:linear-gradient(90deg,#e8f0f3,#d3e1e8);border:1px solid #c9d8df}
.first-visit span{position:absolute;left:60px;top:60px;font-size:20px;letter-spacing:.1em;color:var(--ink)}
.first-visit .photo{right:0;top:0;width:280px;height:158px;background:linear-gradient(90deg,#dbe7ec,#a9b9c2)}

/* banners */
.banner-band{left:0;top:3660px;width:1200px;height:300px;background:var(--beige)}
.banners{left:224px;top:3740px;width:752px;display:flex;gap:2px}
.banner{position:relative;width:250px;height:190px;background:linear-gradient(160deg,#8d9aa6,#4e5a66)}
.banner span{position:absolute;left:50%;top:140px;transform:translateX(-50%);white-space:nowrap;background:rgba(255,255,255,.9);font-size:12px;padding:4px 16px}

/* blog */
.blog-grid{left:220px;top:4120px;width:760px;display:flex;gap:40px}
.blog-card{width:160px;font-size:10px;line-height:1.6}
.blog-card .thumb{width:160px;height:150px;background:#e2e2e2;margin-bottom:8px}
.blog-card time{color:var(--gold)}

/* access */
.access{left:0;top:4500px;width:1200px;height:440px;background:var(--beige)}
.map{left:224px;top:4600px;width:752px;height:300px;background:linear-gradient(135deg,#dfe6d8,#eef0ea 50%,#d4e0ea)}

/* footer */
.footer{left:0;top:4940px;width:1200px;height:432px;background:var(--brown);color:var(--white)}
.f-logo{left:0;top:5000px;width:1200px;justify-content:center;font-size:20px;color:var(--white);letter-spacing:.1em}
.f-hours{left:60px;top:5080px;width:420px;border-collapse:collapse;font-size:11px;background:var(--white);color:var(--ink)}
.f-hours td,.f-hours th{padding:6px 4px;text-align:center;font-weight:400;border-bottom:1px solid var(--line)}
.f-hours th{background:var(--brown-dark);color:var(--white)}
.f-tel{left:60px;top:5210px;font-family:"Cormorant Garamond",serif;font-size:26px;letter-spacing:.08em;color:var(--white)}
.f-addr{left:60px;top:5252px;font-size:10px;color:var(--white)}
.f-nav{left:620px;top:5080px;display:flex;gap:50px;font-size:11px;line-height:2.1;color:var(--white)}
.f-nav ul{list-style:none}
.f-nav li::before{content:"– "}
.copy{left:0;top:5346px;width:1200px;text-align:center;font-size:9px;color:var(--white);opacity:.8}
.pagetop{right:14px;top:4760px;width:44px;height:44px;background:var(--gold)}
</style>
</head>
<body>

<!-- HERO / HEADER -->
<div class="photo hero" role="img" aria-label="木目の壁と診療チェアのある明るい診療室"></div>
<div class="abs header-bar"></div>
<div class="abs logo clinic-name"><i></i>霧野台デンタルクリニック</div>
<nav class="abs gnav"><span>ホーム</span><span>当院について</span><span>医院紹介</span><span>スタッフ紹介</span><span>初めての方へ</span><span>求人情報</span><span>お問い合わせ</span></nav>
<div class="abs tel-btn">tel.092-555-0148</div>
<table class="abs hours">
<tr><th>診療時間</th><th>月</th><th>火</th><th>水</th><th>木</th><th>金</th><th>土</th><th>日</th></tr>
<tr><td>9:00-13:00</td><td>●</td><td>●</td><td>●</td><td>●</td><td>●</td><td>●</td><td>/</td></tr>
<tr><td>14:30-18:30</td><td>●</td><td>●</td><td>/</td><td>●</td><td>●</td><td>▲</td><td>/</td></tr>
</table>
<div class="abs hero-copy">霧野台デンタルクリニック</div>

<!-- NEWS -->
<section class="abs news">
<h2>NEWS</h2>
<ul>
<li><time>2024.08.01</time>夏季休診のお知らせを掲載しました</li>
<li><time>2024.07.15</time>土曜午後の診療時間が変更になります</li>
<li><time>2024.07.01</time>新しい歯科衛生士が着任しました</li>
<li><time>2024.06.20</time>ホームページをリニューアルしました</li>
</ul>
<span class="btn">MORE</span>
</section>

<!-- GREETING -->
<div class="abs greet-panel"></div>
<div class="photo greet-photo" role="img" aria-label="腕を組んで立つ院長の写真"></div>
<section class="abs greet-text">
<h2>GREETING</h2>
<h3>院長挨拶</h3>
<p>霧野台デンタルクリニックのホームページをご覧いただきありがとうございます。</p>
<p>当院は地域の皆様が安心して通える歯科医院を目指しています。</p>
<p>丁寧な説明と痛みの少ない治療を心がけ、一人ひとりに合わせた治療計画をご提案いたします。小さなお子様からご年配の方まで、どなたでもお気軽にご相談ください。</p>
<p>ご来院を心よりお待ちしております。</p>
<p class="sign">霧野台デンタルクリニック 院長　三原 健吾</p>
</section>

<!-- CONCEPT -->
<div class="photo concept" role="img" aria-label="柔らかな光の差す待合室"></div>
<div class="sec-title" style="top:1490px"><span class="en">CONCEPT</span><span class="ja">当院の理念</span></div>
<ol class="abs concept-list">
<li><b>1.</b>みんなが笑顔で過ごせる歯科医院</li>
<li><b>2.</b>痛みの少ない、できるだけ歯を残す治療</li>
<li><b>3.</b>最新の医療設備で安心の診療</li>
</ol>
<span class="abs btn" style="left:540px;top:1730px">MORE</span>

<!-- FEATURES -->
<div class="abs feature-bg"></div>
<div class="sec-title" style="top:1870px"><span class="en">FEATURES</span><span class="ja">当院の特徴</span></div>
<div class="photo feat-photo1" role="img" aria-label="木目調の受付と待合スペース"></div>
<section class="abs feat-box" style="left:600px;top:2100px">
<h3>安心・安らぎの空間の提供</h3>
<p>木目調の落ち着いた院内は、緊張しがちな歯科医院での時間を少しでも心地よく過ごしていただけるよう設計しました。</p>
<p>個室の診療室でプライバシーにも配慮しています。</p>
<span class="btn">MORE</span>
</section>
<div class="photo feat-photo2" role="img" aria-label="間接照明のある診療室の通路"></div>
<section class="abs feat-box" style="left:220px;top:2530px">
<h3>最先端の医療と安心の設備</h3>
<p>最新の診断機器と滅菌設備を導入し、精度の高い治療と安全な環境を整えています。</p>
<p>治療内容はモニターで分かりやすくご説明いたします。</p>
<span class="btn">MORE</span>
</section>

<!-- MEDICAL -->
<div class="photo medical" role="img" aria-label="淡い背景の診療イメージ"></div>
<div class="sec-title" style="top:2990px"><span class="en">MEDICAL</span><span class="ja">診療案内</span></div>
<div class="abs med-grid">
<div class="med-item"><svg width="34" height="34" viewBox="0 0 34 34" fill="none" stroke="#fff" stroke-width="1.5"><path d="M9 6c-4 0-5 5-4 9s2 7 3 13c1 3 3 3 4 0l2-7h4l2 7c1 3 3 3 4 0 1-6 2-9 3-13s0-9-4-9c-3 0-5 2-8 2s-5-2-8-2z"/></svg>銀歯から<br>自然な白い歯へ</div>
<div class="med-item"><svg width="34" height="34" viewBox="0 0 34 34" fill="none" stroke="#fff" stroke-width="1.5"><rect x="5" y="12" width="24" height="14" rx="2"/><path d="M10 12V8h14v4"/></svg>歯医者にいけなく<br>なった方へ</div>
<div class="med-item"><svg width="34" height="34" viewBox="0 0 34 34" fill="none" stroke="#fff" stroke-width="1.5"><path d="M4 17h26M8 12v10M14 12v10M20 12v10M26 12v10"/></svg>歯の色を全体的に<br>白くしたい方へ</div>
<div class="med-item"><svg width="34" height="34" viewBox="0 0 34 34" fill="none" stroke="#fff" stroke-width="1.5"><circle cx="17" cy="17" r="11"/><path d="M12 20c3 3 7 3 10 0"/></svg>口臭・歯茎の<br>違和感が気になる</div>
<div class="med-item"><svg width="34" height="34" viewBox="0 0 34 34" fill="none" stroke="#fff" stroke-width="1.5"><path d="M4 14c8-6 18-6 26 0M4 20c8 6 18 6 26 0"/></svg>歯並びを<br>整えたい方へ</div>
<div class="med-item"><svg width="34" height="34" viewBox="0 0 34 34" fill="none" stroke="#fff" stroke-width="1.5"><path d="M11 5c-4 0-5 5-3 9l3 6h12l3-6c2-4 1-9-3-9-2 0-4 1-6 1s-4-1-6-1zM14 20v9M20 20v9"/></svg>歯を失って<br>しまった方へ</div>
<div class="med-item"><svg width="34" height="34" viewBox="0 0 34 34" fill="none" stroke="#fff" stroke-width="1.5"><circle cx="17" cy="17" r="11"/><circle cx="20" cy="14" r="3"/></svg>虫歯になって<br>しまった方へ</div>
<div class="med-item"><svg width="34" height="34" viewBox="0 0 34 34" fill="none" stroke="#fff" stroke-width="1.5"><circle cx="17" cy="13" r="6"/><path d="M7 29c2-6 18-6 20 0"/></svg>お子様の歯を<br>守りたい方へ</div>
</div>
<div class="abs first-visit">
<span>初めての方へ……</span>
<div class="photo" role="img" aria-label="笑顔の女性患者の写真"></div>
</div>

<!-- BANNERS -->
<div class="abs banner-band"></div>
<div class="abs banners">
<div class="banner" role="img" aria-label="受付スタッフの写真"><span>よくあるご質問</span></div>
<div class="banner" role="img" aria-label="電話対応するスタッフの写真"><span>お問い合わせ</span></div>
<div class="banner" role="img" aria-label="並んだスタッフの写真"><span>求人情報</span></div>
</div>

<!-- BLOG -->
<div class="sec-title" style="top:4030px"><span class="en">BLOG</span><span class="ja">ブログ</span></div>
<div class="abs blog-grid">
<article class="blog-card"><div class="thumb" role="img" aria-label="ブログ記事の写真"></div><time>2024.08.01</time><p>正しい歯みがきの方法をご紹介します</p></article>
<article class="blog-card"><div class="thumb" role="img" aria-label="ブログ記事の写真"></div><time>2024.07.20</time><p>定期検診をおすすめする理由について</p></article>
<article class="blog-card"><div class="thumb" role="img" aria-label="ブログ記事の写真"></div><time>2024.07.05</time><p>お子様の仕上げみがきのポイント</p></article>
<article class="blog-card"><div class="thumb" role="img" aria-label="ブログ記事の写真"></div><time>2024.06.18</time><p>ホワイトニングのよくある疑問</p></article>
</div>
<span class="abs btn" style="left:540px;top:4380px">MORE</span>

<!-- ACCESS -->
<div class="abs access"></div>
<div class="sec-title" style="top:4520px"><span class="en">ACCESS</span><span class="ja">アクセス</span></div>
<div class="photo map" role="img" aria-label="医院周辺の地図"></div>
<div class="abs pagetop"><svg width="44" height="44" viewBox="0 0 44 44" fill="none" stroke="#fff" stroke-width="2"><path d="M14 26l8-8 8 8"/></svg></div>

<!-- FOOTER -->
<footer class="abs footer"></footer>
<div class="abs f-logo clinic-name"><i></i>霧野台デンタルクリニック</div>
<table class="abs f-hours">
<tr><th>診療時間</th><th>月</th><th>火</th><th>水</th><th>木</th><th>金</th><th>土</th><th>日</th><th>祝</th></tr>
<tr><td>9:00〜13:00</td><td>●</td><td>●</td><td>●</td><td>●</td><td>●</td><td>●</td><td>/</td><td>/</td></tr>
<tr><td>14:30〜18:30</td><td>●</td><td>●</td><td>/</td><td>●</td><td>●</td><td>▲</td><td>/</td><td>/</td></tr>
</table>
<div class="abs f-tel">tel.092-555-0148</div>
<div class="abs f-addr">〒000-0000　霧野台市中央区1-2-3　駐車場完備</div>
<nav class="abs f-nav">
<ul><li>ホーム</li><li>当院について</li><li>医院紹介</li><li>スタッフ紹介</li><li>初めての方へ</li><li>求人情報</li><li>よくあるご質問</li></ul>
<ul><li>銀歯から自然な白い歯へ</li><li>歯医者にいけなくなった方へ</li><li>歯の色を白くしたい方へ</li><li>口臭・歯茎が気になる方へ</li><li>歯並びを整えたい方へ</li><li>歯を失ってしまった方へ</li></ul>
<ul><li>虫歯になってしまった方へ</li><li>お子様の歯を守りたい方へ</li><li>お知らせ</li><li>ブログ</li><li>お問い合わせ</li></ul>
</nav>
<div class="abs copy">Copyright © 霧野台デンタルクリニック All Rights Reserved.</div>

</body>
</html>
```